Marketing Brochure, Sales Brochure, Mailings

We need a brochure for our company. VRELM Holdings Inc. is a construction bond broker. You can view information on our company at www.vrelmsurety.example. We will be utilizing this brochure for sales marketing. We will be sending it to companies that don't know anything about VRELM, so these are "cold" prospects. The intention of the brochure is to provide information to the prospect in hopes that they will contact us for more information on our services. We are selling a service and do not have any physical products. The people that we are sending these brochures to are required to use what we sell but are currently using a competitor. Our value added and sales pitch is better service, lower rates, high capacity, no collateral, no escrow.

Target Market(s)

Construction Companies that work on Public funded projects

Industry/Entity Type

Construction

Requirements
Must have
• Company Logo, Construction related info, components from website.
Should not have
• Things related to residential construction

```html
<!DOCTYPE html>
<html lang="en">
<head>
<meta charset="utf-8">
<title>VRELM Holdings Inc. – Construction Bond Brochure</title>
<link href="https://fonts.googleapis.com/css2?family=Montserrat:wght@600;700;800&family=Open+Sans:wght@400;600&display=swap" rel="stylesheet">
<style>
:root{
  --orange:#f7941d;
  --orange-dark:#e07a10;
  --navy:#34404f;
  --slate:#5b6775;
  --grey:#9aa3ac;
  --light:#e9ecef;
  --paper:#ffffff;
  --stage:#d9dde1;
  --text:#3f4650;
  --photo-sky:#9fb4c8;
  --photo-site:#7d8a96;
}
*{box-sizing:border-box;margin:0;padding:0}
html,body{width:1200px;height:3860px;overflow:hidden;background:var(--stage)}
body{font-family:"Open Sans",Arial,sans-serif;color:var(--text);display:flex;flex-direction:column;justify-content:center;gap:80px}
.spread{position:relative;width:1200px;height:927px;background:var(--paper);overflow:hidden}
.spread .deco{position:absolute;inset:0}
.panel{position:absolute;top:0;width:400px;height:927px}
.p1{left:0}.p2{left:400px}.p3{left:800px}
.photo{position:absolute}
h2.section{font-family:"Montserrat",Arial,sans-serif;font-weight:700;color:var(--navy);font-size:22px;display:flex;align-items:center;gap:10px;text-transform:none}
h2.section::before{content:"";width:16px;height:16px;background:var(--orange);flex:none}
h2.caps{text-transform:uppercase;letter-spacing:1px}
.rule{height:3px;background:var(--orange);margin:8px 0 14px}
p.body{font-size:12.5px;line-height:1.62;text-align:justify}
ul.list{list-style:none;font-size:13px;line-height:1.75}
ul.list li{display:flex;align-items:center;gap:8px}
ul.list li::before{content:"";width:7px;height:7px;background:var(--orange);flex:none}
.brand{display:flex;align-items:center;gap:10px;font-family:"Montserrat",Arial,sans-serif;font-weight:800;font-size:34px;color:var(--navy);letter-spacing:2px}
.brand .mark{width:28px;height:28px;background:var(--orange)}
.staff{font-size:11.5px;line-height:1.45;color:var(--slate)}
.staff b{display:block;color:var(--orange);font-weight:600}
.contact-cta{font-family:"Montserrat",Arial,sans-serif;font-weight:700;color:#fff;font-size:22px;text-align:center;line-height:1.3}
.contact-cta span{color:var(--orange)}
.details{display:grid;grid-template-columns:auto 1fr;gap:6px 12px;font-size:12.5px;color:var(--navy);align-items:center}
.details svg{width:16px;height:16px}
.slogan{font-family:"Montserrat",Arial,sans-serif;font-weight:700;color:#fff;font-size:17px;line-height:1.35}
.url{font-family:"Montserrat",Arial,sans-serif;font-weight:700;color:var(--navy);font-size:24px}
.visit{position:absolute;left:0;right:0;bottom:0;height:46px;background:var(--orange);color:#fff;display:flex;justify-content:space-between;align-items:center;padding:0 28px;font-family:"Montserrat",Arial,sans-serif;font-weight:700;font-size:15px}
</style>
</head>
<body>

<!-- Outside spread -->
<section class="spread outside">
  <svg class="deco" viewBox="0 0 1200 927" aria-hidden="true">
    <path d="M0 700 C300 640 820 650 1200 600 L1200 927 L0 927Z" fill="var(--light)"/>
    <path d="M0 690 C300 630 820 640 1200 590 L1200 600 C820 650 300 640 0 700Z" fill="var(--orange)"/>
  </svg>

  <div class="panel p1">
    <div style="position:absolute;left:34px;top:40px;width:332px">
      <h2 class="section caps">About Us</h2>
      <div class="rule"></div>
      <p class="body">VRELM Holdings Inc. was established in 1990 by Dana Whitcombe, President and owner. With three decades of experience in the surety industry, she provides extensive technical and underwriting capabilities to the company and its clients. The entire staff of VRELM Holdings Inc. is committed to the goals and objectives of the agency and works to put their clients in a profitable and client-centered position. VRELM has unique abilities to help a contractor analyze their management system and to assist them in addressing deficiencies. With access to over 50 surety markets, VRELM is able to match your business needs with one of our markets, delivering better service, lower rates, high capacity, no collateral and no escrow.</p>
    </div>
    <div class="photo" role="img" aria-label="Photo of construction workers on a public works site" style="left:0;top:716px;width:400px;height:211px;background:linear-gradient(160deg,var(--photo-sky),var(--photo-site));clip-path:path('M0 0 C140 -10 280 -20 400 -34 L400 211 L0 211Z')"></div>
  </div>

  <div class="panel p2">
    <div style="position:absolute;left:30px;top:44px;display:flex;gap:14px">
      <div role="img" aria-label="Portrait of the company president" style="width:78px;height:98px;background:linear-gradient(180deg,#c9ced4,#8c96a1);border:3px solid var(--light)"></div>
      <div class="staff">
        <b>Dana Whitcombe – President</b>dana@vrelmsurety.example<br><br>
        <b>Marcus Lindqvist – Underwriting</b>marcus@vrelmsurety.example<br><br>
        <b>Priya Okafor – Account Manager</b>priya@vrelmsurety.example
      </div>
    </div>
    <div style="position:absolute;left:0;top:700px;width:400px;height:90px;background:var(--navy);display:flex;align-items:center;justify-content:center">
      <p class="contact-cta">Contact Us Now:<br><span>www.vrelmsurety.example</span></p>
    </div>
    <div style="position:absolute;left:30px;top:808px;display:flex;gap:24px;align-items:flex-start">
      <p style="font-family:'Montserrat',Arial,sans-serif;font-weight:700;font-size:13px;color:var(--navy);padding-top:34px">Contact Details</p>
      <div class="details">
        <svg viewBox="0 0 16 16"><path d="M4 1l3 3-2 2c1 2 3 4 5 5l2-2 3 3-2 3C7 14 2 9 1 3z" fill="var(--orange)"/></svg><span>555-0142</span>
        <svg viewBox="0 0 16 16"><rect x="2" y="5" width="12" height="8" fill="var(--orange)"/><rect x="5" y="2" width="6" height="4" fill="var(--slate)"/></svg><span>555-0178</span>
        <svg viewBox="0 0 16 16"><rect x="1" y="3" width="14" height="10" fill="var(--orange)"/><path d="M1 3l7 6 7-6" stroke="#fff" fill="none"/></svg><span>info@vrelmsurety.example</span>
        <svg viewBox="0 0 16 16"><path d="M8 1a5 5 0 0 1 5 5c0 4-5 9-5 9S3 10 3 6a5 5 0 0 1 5-5z" fill="var(--orange)"/><circle cx="8" cy="6" r="2" fill="#fff"/></svg><span>48 Harbor Point Dr, Suite 210, Lakemont</span>
      </div>
    </div>
  </div>

  <div class="panel p3">
    <div class="brand" style="position:absolute;right:34px;top:34px"><span class="mark"></span>VRELM</div>
    <div class="photo" role="img" aria-label="Construction engineer in hard hat and safety vest working at a laptop" style="left:30px;top:120px;width:350px;height:480px;border-radius:50% 50% 46% 46%/44% 44% 40% 40%;background:radial-gradient(circle at 50% 40%,#f2c28a,#a9b5c1 55%,#6f7c89);border:6px solid var(--light)"></div>
    <div style="position:absolute;left:0;top:640px;width:400px;height:92px;background:var(--orange);clip-path:polygon(0 22%,100% 0,100% 78%,0 100%);display:flex;align-items:center;padding:0 30px">
      <p class="slogan">Your Slogan – Bonding built for public<br>works contractors, done right.</p>
    </div>
    <p class="url" style="position:absolute;right:30px;bottom:50px">www.vrelmsurety.example</p>
  </div>
</section>

<!-- Inside spread -->
<section class="spread inside">
  <svg class="deco" viewBox="0 0 1200 927" aria-hidden="true">
    <path d="M0 300 C120 340 260 330 400 290 L400 308 C260 348 120 358 0 318Z" fill="var(--orange)"/>
    <path d="M0 800 C160 760 300 770 400 740 L400 927 L0 927Z" fill="var(--light)"/>
  </svg>

  <div class="panel p1">
    <div class="photo" role="img" aria-label="Steel scaffolding and crane on a commercial building site" style="left:0;top:0;width:400px;height:305px;background:linear-gradient(180deg,var(--photo-sky),var(--photo-site));clip-path:path('M0 0 L400 0 L400 290 C260 330 120 340 0 300Z')"></div>
    <div style="position:absolute;left:34px;top:352px;width:332px">
      <h2 class="section">About Bonds</h2>
      <div class="rule"></div>
      <p class="body">A surety bond is a three-party agreement between the contractor (principal), the owner (obligee) and the surety company (guarantor). In construction, bonds come in three main types: bid bonds, performance bonds and payment bonds. A bid bond shows the owner that the contractor is qualified and will sign the contract if awarded. A performance bond protects the owner should the contractor fail to complete the work as agreed. A payment bond guarantees that subcontractors and suppliers will be paid. A bond is not insurance for the contractor; it is a credit relationship, and the contractor stays responsible to the surety.</p>
    </div>
    <div class="photo" role="img" aria-label="Construction worker in hard hat on site" style="left:0;top:760px;width:400px;height:167px;background:linear-gradient(160deg,#b8c3cd,var(--photo-site));clip-path:path('M0 40 C160 0 300 10 400 -20 L400 167 L0 167Z')"></div>
  </div>

  <div class="panel p2">
    <div class="photo" role="img" aria-label="Tall crane and building frame against the sky" style="left:0;top:0;width:400px;height:250px;background:linear-gradient(180deg,#b4c6d6,var(--photo-site))"></div>
    <div style="position:absolute;left:0;top:250px;width:400px;height:8px;background:var(--orange)"></div>
    <div style="position:absolute;left:34px;top:290px;width:332px">
      <h2 class="section">How This Works</h2>
      <div class="rule"></div>
      <ul class="list">
        <li>Bid Bonds</li><li>Performance Bonds</li><li>Payment Bonds</li><li>Maintenance Bonds</li>
      </ul>
      <h2 class="section" style="margin-top:22px">Bondable Trades</h2>
      <div class="rule"></div>
      <ul class="list" style="columns:2">
        <li>Asbestos</li><li>Concrete</li><li>Design / Build</li><li>Electrical</li><li>Environmental</li><li>Excavation</li><li>General Contractor</li><li>Heavy / Highway</li><li>Mechanical</li><li>Paving</li><li>Plumbing</li><li>Roofing</li><li>Specialty Trades</li><li>Sewer / Water</li><li>Subdivision / Site Improvement</li>
      </ul>
    </div>
    <div class="brand" style="position:absolute;left:34px;top:820px;font-size:28px"><span class="mark" style="width:24px;height:24px"></span>VRELM</div>
    <div class="photo" role="img" aria-label="Site worker reviewing plans" style="left:230px;top:760px;width:170px;height:167px;background:linear-gradient(160deg,#c5ced6,var(--photo-site))"></div>
  </div>

  <div class="panel p3">
    <div class="photo" role="img" aria-label="Highway bridge under construction" style="left:0;top:0;width:400px;height:200px;background:linear-gradient(180deg,#a8bfd4,#8b97a2)"></div>
    <div style="position:absolute;left:0;top:200px;width:400px;height:8px;background:var(--orange)"></div>
    <div style="position:absolute;left:34px;top:232px;width:332px">
      <h2 class="section">Bonds We Specialize In</h2>
      <div class="rule"></div>
      <ul class="list" style="font-size:12.5px">
        <li>Standard Surety – Bonds up to $25,000,000</li>
        <li>Specialty Surety – Bonds up to $15,000,000</li>
        <li>SBA Bonds</li>
        <li>Small &amp; Weaker Credit Contractors</li>
        <li>Express Bonds – Bonds up to $500,000</li>
        <li>Start-Up Companies</li>
      </ul>
      <h2 class="section" style="margin-top:20px">SBA Bonds</h2>
      <div class="rule"></div>
      <p class="body">The SBA Surety Bond Guarantee Program was developed to provide small, minority and emerging contractors access to surety bonds. The program is sponsored and administered by a federal agency. VRELM Holdings Inc. is a leading agent in the program, helping contractors qualify with less paperwork.</p>
      <h2 class="section" style="margin-top:20px">Express Bonds</h2>
      <div class="rule"></div>
      <p class="body">VRELM Holdings Inc. can provide bid, performance and payment bonds for contracts up to $500,000 based on personal credit scores. We can also provide aggregate limits up to $1,000,000 with limited paperwork, helping you start bidding right away.</p>
    </div>
    <div class="visit"><span>Please visit</span><span>www.vrelmsurety.example</span></div>
  </div>
</section>

</body>
</html>
```